Stationary and Business Card for Talbe Media Company
Include Invoice, DVD and Binder template
Stationary and Business Card for Talbe Media Company -
Creative Brief
Use specific fonts
Prefer font name "neometric" ... you suggest
Professional
K. Morwenel
Sales Director
P. O. Box No 47318, Lam Fung Wan, Kowloon, Hong Kong
morwenel@talbe.example
www.talbe.example
at the back of the business card add the following tag "Digital Media Technology Source" make sure it is at one side in a small font . It can also, be added to the Stationaries.
In the Company's logo the letter "O" reflects our business .. we can have the "O" occupies most of the back and add to it the tag "Digital Media Technology Source" in a small font. you suggest

```html
<!DOCTYPE html>
<html lang="en">
<head>
<meta charset="utf-8">
<title>Talbe Media Company – Stationery Set</title>
<link rel="stylesheet" href="https://fonts.googleapis.com/css2?family=Questrial&display=swap">
<style>
  :root{
    --backdrop:#6e3d2b;
    --paper:#ffffff;
    --grey-light:#e6e6e6;
    --grey-mid:#b9b9b9;
    --grey-dark:#5a5a5a;
    --charcoal:#3b3b3b;
    --brand-red:#c4161c;
    --brand-red-dark:#8e0f13;
    --ink:#555555;
  }
  *{margin:0;padding:0;box-sizing:border-box}
  html,body{width:1200px;height:389px;overflow:hidden}
  body{background:var(--backdrop);font-family:"Questrial",sans-serif;color:var(--ink)}
  .canvas{position:relative;width:1200px;height:389px}
  .item{position:absolute;background:var(--paper);box-shadow:0 2px 6px rgba(0,0,0,.35);overflow:hidden}
  .brand{position:absolute;color:var(--brand-red);font-size:15px;line-height:1;letter-spacing:.5px}
  .tag{position:absolute;font-size:4px;color:var(--grey-dark);white-space:nowrap}
  .mark{position:absolute;border-radius:50%}
  .mark--faint{background:var(--grey-light)}
  .mark--dark{background:var(--charcoal)}
  .small{position:absolute;font-size:3.5px;line-height:1.4;color:var(--ink);white-space:nowrap}

  /* business card stack top-left */
  .card-front{left:12px;top:43px;width:67px;height:44px}
  .card-front .brand{left:6px;top:6px;font-size:11px}
  .card-back{left:12px;top:96px;width:67px;height:26px;background:var(--grey-light)}
  .card-back .mark{right:6px;top:5px;width:16px;height:16px}

  /* letterhead */
  .letterhead{left:96px;top:36px;width:149px;height:180px}
  .letterhead .brand{left:10px;top:10px;font-size:13px}
  .letterhead .tag{left:10px;top:25px}
  .letterhead .mark{right:8px;bottom:18px;width:44px;height:44px}
  .letterhead .small{left:10px;bottom:6px}

  /* portrait envelope */
  .envelope{left:281px;top:36px;width:151px;height:276px}
  .envelope .flap{position:absolute;left:0;top:0;width:100%;height:22px;background:linear-gradient(var(--grey-dark),var(--charcoal))}
  .envelope .brand{left:10px;top:32px;font-size:16px}
  .envelope .tag{left:10px;top:50px}
  .envelope .mark{right:8px;bottom:48px;width:70px;height:70px;border:4px solid var(--brand-red)}
  .envelope .small{left:10px;bottom:36px}

  /* folders */
  .folder{top:43px;height:312px;display:flex}
  .folder-open{left:473px;width:336px}
  .folder-closed{left:833px;width:353px}
  .panel{position:relative;flex:1;background:radial-gradient(circle at 50% 40%,#f5f5f5,var(--grey-mid))}
  .panel--white{background:var(--paper)}
  .panel + .panel{border-left:1px solid #cfcfcf}
  .panel .brand{left:14px;top:14px;font-size:22px}
  .panel .tag{left:14px;top:36px}
  .pocket{position:absolute;left:0;right:0;bottom:0;height:105px;background:linear-gradient(#f2f2f2,#d8d8d8);border-top:3px solid var(--brand-red)}
  .pocket .brand{left:50%;top:24px;transform:translateX(-50%);font-size:20px}
  .panel .footer-tag{position:absolute;left:0;right:0;bottom:108px;text-align:center;font-size:4px;color:var(--grey-dark)}
  .folder-open .mark{right:10px;bottom:112px;width:30px;height:30px}
  .folder-closed .mark{right:12px;top:70px;width:90px;height:90px;background:rgba(150,150,150,.35)}

  /* DL envelope */
  .dl-envelope{left:10px;top:259px;width:170px;height:108px}
  .dl-envelope .top{position:absolute;left:0;top:0;width:100%;height:26px;background:var(--grey-light)}
  .dl-envelope .brand{left:8px;top:6px;font-size:13px}
  .dl-envelope .mark{right:10px;bottom:10px;width:42px;height:42px;border:3px solid var(--brand-red)}
  .dl-envelope .small{left:50px;top:52px}

  /* disc */
  .disc{position:absolute;left:192px;top:274px;width:80px;height:80px;border-radius:50%;
    background:radial-gradient(circle,var(--backdrop) 0 5px,#eeeeee 6px 12px,var(--brand-red) 13px 22px,#f4f4f4 23px);
    box-shadow:0 2px 6px rgba(0,0,0,.35)}

  /* business cards */
  .card-red{left:276px;top:283px;width:108px;height:48px;background:linear-gradient(var(--brand-red),var(--brand-red-dark))}
  .card-red .brand{left:8px;top:8px;color:var(--paper);font-size:13px}
  .card-red .tag{left:8px;bottom:5px;color:#f3d0d0}
  .card-white{left:276px;top:336px;width:108px;height:38px}
  .card-white .brand{left:8px;top:6px;font-size:11px}
  .card-white .small{left:8px;top:20px}
  .card-side{left:388px;top:288px;width:73px;height:67px}
  .card-side .mark{left:50%;top:9px;width:40px;height:40px;transform:translateX(-50%)}
  .card-side .tag{left:0;right:0;bottom:6px;text-align:center}
</style>
</head>
<body>
<main class="canvas">

  <section class="item card-front" aria-label="Business card front">
    <span class="brand">talbe</span>
    <p class="small" style="left:6px;top:22px">K. Morwenel<br>Sales Director</p>
  </section>
  <section class="item card-back" aria-label="Business card back">
    <span class="mark mark--dark"></span>
  </section>

  <section class="item letterhead" aria-label="Letterhead">
    <span class="brand">talbe</span>
    <span class="tag">Digital Media Technology Source</span>
    <span class="mark mark--faint"></span>
    <p class="small">P. O. Box No 47318, Lam Fung Wan, Kowloon, Hong Kong<br>morwenel@talbe.example · www.talbe.example</p>
  </section>

  <section class="item envelope" aria-label="Envelope">
    <div class="flap"></div>
    <span class="brand">talbe</span>
    <span class="tag">Digital Media Technology Source</span>
    <p class="small">P. O. Box No 47318, Lam Fung Wan, Kowloon, Hong Kong</p>
    <span class="mark mark--dark"></span>
  </section>

  <section class="item folder folder-open" aria-label="Presentation folder, open">
    <div class="panel">
      <p class="footer-tag">Digital Media Technology Source</p>
      <div class="pocket"></div>
    </div>
    <div class="panel panel--white">
      <span class="brand">talbe</span>
      <span class="tag">Digital Media Technology Source</span>
      <span class="mark mark--dark"></span>
      <div class="pocket"><span class="brand">talbe</span></div>
    </div>
  </section>

  <section class="item folder folder-closed" aria-label="Presentation folder, cover and back">
    <div class="panel">
      <p class="footer-tag">www.talbe.example</p>
      <div class="pocket" style="border-top-width:2px"></div>
    </div>
    <div class="panel">
      <span class="mark"></span>
      <p class="footer-tag">Digital Media Technology Source</p>
      <div class="pocket" style="border-top-width:2px"></div>
    </div>
  </section>

  <section class="item dl-envelope" aria-label="DL envelope">
    <div class="top"></div>
    <span class="brand">talbe</span>
    <p class="small">P. O. Box No 47318, Lam Fung Wan, Kowloon, Hong Kong</p>
    <span class="mark mark--dark"></span>
  </section>

  <div class="disc" aria-label="DVD disc"></div>

  <section class="item card-red" aria-label="Business card, red side">
    <span class="brand">talbe</span>
    <span class="tag">Digital Media Technology Source</span>
  </section>
  <section class="item card-white" aria-label="Business card, contact side">
    <span class="brand">talbe</span>
    <p class="small">K. Morwenel · Sales Director<br>morwenel@talbe.example · www.talbe.example</p>
  </section>
  <section class="item card-side" aria-label="Business card back with tag">
    <span class="mark mark--faint"></span>
    <span class="tag">Digital Media Technology Source</span>
  </section>

</main>
</body>
</html>
```